New Technology Training Center needs a POSTER design

I am looking for posters to describe the opening of a new technology training center.
MOSTLY ADULT TRAINING PLEASE ADD IN THE POSTER ADULTS WORKING
ON ELECTRONICS AND WORK TRAINING.
These posters will go outside of the building.
Also adults learning fabrication, working on pcb boards at work stations.
Please visit web site to get ideas (www.ruxolearnhub.com)

I would like something creative.
I attached a simple poster similar to the kind of poster I am looking for.

Target Market(s)

People would like to take technology training

Industry/Entity Type

Computer Training

Font styles to use
Sans Serif

Requirements
Must have
• Lots of colors and a lot of people from the inter city like African Americans and Hispanics.
Nice to have
• NEED MORE ADULT POSTERS DESIGNED
Should not have
• Computers in design its to common

```html
<!DOCTYPE html>
<html lang="en">
<head>
<meta charset="utf-8">
<title>RUXO Adult Tech Training – Grand Opening</title>
<link rel="stylesheet" href="https://fonts.googleapis.com/css2?family=Anton&family=Bangers&family=Oswald:wght@500;700&family=Lato:wght@700;900&display=swap">
<style>
  :root{
    --page:#e9e9e7;
    --sun:#fff9c2;
    --yellow:#f7e56a;
    --gold:#f3cf4e;
    --green:#3aa51e;
    --green-dark:#0d3d06;
    --pink:#c8155e;
    --ink:#141414;
    --band:#111111;
    --url:#ffc21a;
    --frame:#ffffff;
  }
  *{margin:0;padding:0;box-sizing:border-box}
  html,body{width:1200px;height:897px;overflow:hidden;background:var(--page)}
  .flyer{
    position:absolute;left:300px;top:24px;width:600px;height:848px;overflow:hidden;
    background:
      radial-gradient(ellipse at 50% 72%, var(--sun) 0%, rgba(255,249,194,0) 45%),
      linear-gradient(180deg,var(--yellow) 0%,#f6ec8a 40%,#d9ea78 55%,var(--yellow) 80%,var(--gold) 100%);
    box-shadow:0 14px 30px rgba(0,0,0,.25);
  }
  .sunburst{
    position:absolute;left:0;top:300px;width:600px;height:548px;
    background:repeating-conic-gradient(from 0deg at 50% 62%, rgba(255,255,255,.55) 0deg 6deg, rgba(255,255,255,0) 6deg 15deg);
    -webkit-mask:radial-gradient(circle at 50% 62%, #000 0%, #000 35%, transparent 75%);
            mask:radial-gradient(circle at 50% 62%, #000 0%, #000 35%, transparent 75%);
  }
  .side-glow{position:absolute;top:380px;height:260px;width:180px;background:radial-gradient(ellipse at center,rgba(120,200,50,.7),rgba(120,200,50,0) 70%)}
  .side-glow.left{left:-80px}.side-glow.right{right:-80px}
  .hero-photo{
    position:absolute;left:0;top:0;width:600px;height:420px;
    background:
      linear-gradient(90deg,rgba(247,229,106,0) 0%,rgba(247,229,106,0) 55%,rgba(250,240,150,.95) 80%,#fbf3a6 100%),
      linear-gradient(180deg,#6a5634 0%,#8a6a40 35%,#3a56c8 62%,#c7a04a 85%,rgba(247,229,106,0) 100%);
  }
  .brand{
    position:absolute;right:46px;top:130px;
    font-family:"Oswald",sans-serif;font-weight:700;font-size:66px;letter-spacing:2px;color:var(--ink);
  }
  .snap{position:absolute;border:5px solid var(--frame);box-shadow:0 4px 10px rgba(0,0,0,.35)}
  .snap.pcb{left:18px;top:330px;width:178px;height:120px;transform:rotate(2deg);background:linear-gradient(135deg,#8a5a3c,#b57a52 45%,#2f6b3a)}
  .snap.fab{left:196px;top:352px;width:226px;height:160px;transform:rotate(5deg);background:linear-gradient(135deg,#d9d4cc,#8a5e40 45%,#2a3a6a 80%);z-index:2}
  .snap.bench{left:414px;top:380px;width:172px;height:112px;transform:rotate(3deg);background:linear-gradient(135deg,#efefe9,#7a6048 45%,#6bbf3a 75%,#3b2a20);z-index:1}
  .title{position:absolute;left:0;width:600px;text-align:center;white-space:nowrap}
  .title.main{
    top:528px;font-family:"Anton",sans-serif;font-size:54px;line-height:1;color:var(--green);
    -webkit-text-stroke:2px var(--green-dark);
    text-shadow:3px 3px 0 var(--green-dark);
  }
  .title.sub{
    top:592px;font-family:"Bangers",sans-serif;font-size:48px;line-height:1;color:var(--pink);letter-spacing:3px;
    text-shadow:-2px -2px 0 #fff,2px -2px 0 #fff,-2px 2px 0 #fff,2px 2px 0 #fff,4px 4px 0 rgba(0,0,0,.2);
  }
  .meta{
    position:absolute;left:0;width:600px;top:652px;display:flex;justify-content:center;align-items:center;gap:14px;
  }
  .ages{font-family:"Oswald",sans-serif;font-weight:700;font-size:24px;line-height:.95;color:var(--ink);text-align:center}
  .divider{width:2px;height:46px;background:var(--ink)}
  .year{font-family:"Oswald",sans-serif;font-weight:700;font-size:54px;line-height:1;color:var(--ink)}
  .year .accent{color:var(--pink)}
  .tagline{
    position:absolute;left:0;width:600px;top:724px;font-family:"Lato",sans-serif;font-weight:900;font-size:13px;line-height:1.2;color:var(--ink);
    text-align:center;letter-spacing:.3px;
  }
  .register-band{position:absolute;left:0;bottom:0;width:600px;height:82px}
  .register-band svg{position:absolute;inset:0}
  .register-text{
    position:absolute;left:0;width:600px;top:26px;text-align:center;font-family:"Oswald",sans-serif;font-weight:700;font-size:24px;line-height:1;color:#fff;
    transform:skewX(-8deg);white-space:nowrap;
  }
  .register-text .url{color:var(--url)}
</style>
</head>
<body>
  <main class="flyer">
    <div class="sunburst"></div>
    <div class="side-glow left"></div>
    <div class="side-glow right"></div>
    <div class="hero-photo" role="img" aria-label="Photo of an adult trainee in safety goggles soldering parts at an electronics workstation"></div>
    <div class="brand">RUXO</div>

    <div class="snap pcb" role="img" aria-label="Photo of adults assembling a printed circuit board together"></div>
    <div class="snap fab" role="img" aria-label="Photo of an adult learner working on fabrication equipment"></div>
    <div class="snap bench" role="img" aria-label="Photo of a smiling adult trainee at an electronics work bench"></div>

    <h1 class="title main">ADULT TECH TRAINING</h1>
    <h2 class="title sub">GRAND OPENING</h2>

    <div class="meta">
      <div class="ages">AGES<br>18+</div>
      <div class="divider"></div>
      <div class="year">20<span class="accent">16</span></div>
    </div>

    <p class="tagline">ELECTRONICS, PCB AND FABRICATION WORK TRAINING<br>NOW OPEN AT RUXO LEARN HUB</p>

    <div class="register-band">
      <svg width="600" height="82" viewBox="0 0 600 82" aria-hidden="true">
        <polygon points="0,22 36,0 564,0 600,22 600,82 0,82" fill="var(--band)"/>
      </svg>
      <p class="register-text">To register visit us at <span class="url">www.ruxolearnhub.com</span></p>
    </div>
  </main>
</body>
</html>
```